myQuikTrade Webdesign - trading your electronics for cash - helping you clear up clutter

We need web design (and an updated logo) for a new company based in London called "myQuikTrade". It is a platform that enables users to sell their old electronics for cash, either for themselves or they can donate the cash to charity. In time, we also plan to enable buying of electronics on the site. We specialise in mobile phones, tablets, laptops, and games consoles. Please review pirrowen.com, which is a US site with the same business, and also tunderbrook.co.uk, so have a similar business in the UK. We would like to see designs that use the colour red, and that are bold. We currently have a logo, and a WIP site built, but the design needs to be dramatically improved, the right colour mix needs to be chosen to give a clean and modern feel. Please review www.myquiktrade.com to get an understanding of the work that needs to be improved.

Target Market(s)

People who buy electronics frequently, i.e. upgrade every time a new quince product comes out! These guys usually have a lap top, desk top, tablet and phone.

Industry/Entity Type

Electronics

Logo Text

myQuikTrade

Number of Pages Required

3 page

Font styles to use
Sans Serif

Colors
ec1f27

Requirements
Must have
• Home page design
• "How-it-works" page design
• Sell page design
• Must use the colour red, and have a secondary/accent colour.

```html
<!DOCTYPE html>
<html lang="en">
<head>
<meta charset="utf-8">
<title>myQuikTrade – Sell your electronics for cash</title>
<link rel="stylesheet" href="https://fonts.googleapis.com/css2?family=Raleway:wght@500;600;700&family=Open+Sans:wght@400;600;700&display=swap">
<style>
:root{
  --red:#ec1f27;
  --red-dark:#c8141b;
  --navy:#3d3a5c;
  --navy-deep:#2f2d49;
  --ink:#333333;
  --muted:#7a7a7a;
  --light:#f0f0f2;
  --footer:#1f1f1f;
  --footer-text:#d6d6d6;
  --white:#ffffff;
}
*{box-sizing:border-box;margin:0;padding:0}
html,body{width:1200px;height:2413px;overflow:hidden;background:var(--white)}
body{position:relative;font-family:"Open Sans",Arial,sans-serif;color:var(--ink)}
.abs{position:absolute}
.topline{left:0;top:0;width:1200px;height:5px;background:var(--navy-deep)}
/* header */
.header{left:0;top:5px;width:1200px;height:111px;background:var(--white)}
.brand{display:flex;align-items:center;gap:10px}
.brand-mark{width:26px;height:26px;background:var(--red)}
.brand-name{font-family:"Raleway",sans-serif;font-weight:600;font-size:26px;color:var(--navy)}
.nav-link{font-family:"Raleway",sans-serif;font-size:16px;color:var(--ink);font-weight:500}
.btn-nav{display:flex;align-items:center;justify-content:center;font-family:"Raleway",sans-serif;font-weight:700;font-size:16px;border:2px solid}
.btn-buy{color:var(--red);border-color:var(--red)}
.btn-sell{color:var(--navy);border-color:var(--navy)}
.btn-login{background:var(--red);color:var(--white);font-family:"Raleway",sans-serif;font-size:14px;font-weight:600;display:flex;align-items:center;justify-content:center;gap:8px}
/* hero */
.hero{left:0;top:116px;width:1200px;height:519px;overflow:hidden}
.hero-photo{left:0;top:0;width:1200px;height:519px;background:linear-gradient(100deg,#9a6b5b 0%,#b7a59a 45%,#6f8fb0 65%,#c9b9a6 85%,#8a7a6c 100%)}
.hero-red{left:0;top:0;width:1200px;height:519px}
.hero-art{left:158px;top:100px;width:320px;height:180px;background:linear-gradient(180deg,rgba(255,255,255,.22),rgba(255,255,255,.08));border-radius:4px}
.hero-text{left:60px;top:300px;width:514px;text-align:center;color:var(--white);font-size:13.5px;line-height:23px}
.btn-hero{top:373px;height:43px;width:137px;background:var(--navy);border:2px solid var(--white);color:var(--white);font-family:"Raleway",sans-serif;font-weight:600;font-size:16px;display:flex;align-items:center;justify-content:center;letter-spacing:1px}
.hero-or{left:308px;top:387px;color:var(--white);font-size:12px;font-family:"Raleway",sans-serif}
/* sections */
.sec-title{width:1200px;left:0;text-align:center;font-family:"Raleway",sans-serif;font-weight:700;font-size:26px;color:var(--ink);letter-spacing:.3px}
.sec-text{left:220px;width:760px;text-align:center;font-size:12px;line-height:24px;color:var(--muted)}
.gadget{width:126px;height:126px;border-radius:50%;border:2px solid #d8d8de;display:flex;align-items:center;justify-content:center;top:814px}
.gadget-inner{width:116px;height:116px;border-radius:50%;background:var(--navy);display:flex;align-items:center;justify-content:center}
.how{left:0;top:993px;width:1200px;height:278px;background:var(--light)}
.btn-red{background:var(--red);color:var(--white);font-family:"Raleway",sans-serif;font-weight:700;font-size:14px;display:flex;align-items:center;justify-content:center;letter-spacing:.5px}
/* app */
.app{left:0;top:1271px;width:1200px;height:381px;background:linear-gradient(90deg,#3a3858 0%,#46446a 50%,#3a3858 100%)}
.app-title{left:166px;top:1354px;font-family:"Raleway",sans-serif;font-weight:700;font-size:25px;color:var(--white)}
.app-text{left:166px;top:1398px;width:520px;font-size:12.5px;line-height:25px;color:var(--white)}
.store-badge{top:1520px;width:150px;height:42px;background:#111;border:1px solid #777;border-radius:6px}
.app-device{left:692px;top:1287px;width:290px;height:365px;background:linear-gradient(160deg,#f4f4f4 0%,#e0d2c8 55%,#c9a993 100%);opacity:.9}
/* why */
.feature{width:340px;text-align:center}
.feature h3{font-family:"Open Sans",sans-serif;font-weight:700;font-size:14px;color:var(--ink);margin-bottom:14px;letter-spacing:.2px}
.feature p{font-size:12px;line-height:23px;color:#666}
/* newsletter */
.news{left:0;top:2032px;width:1200px;height:85px;background:var(--red)}
.news-small{left:163px;top:2049px;color:var(--white);font-family:"Raleway",sans-serif;font-weight:700;font-size:13px;letter-spacing:.5px}
.news-big{left:163px;top:2069px;color:var(--white);font-family:"Raleway",sans-serif;font-weight:700;font-size:20px;letter-spacing:.5px}
.news-input{left:347px;top:2053px;width:623px;height:38px;background:var(--white);color:#999;font-size:11px;padding-left:26px;display:flex;align-items:center;letter-spacing:.5px}
.news-btn{left:988px;top:2053px;width:115px;height:38px;border:2px solid var(--white);color:var(--white);font-family:"Raleway",sans-serif;font-weight:700;font-size:13px;display:flex;align-items:center;justify-content:center}
/* footer */
.footer{left:0;top:2117px;width:1200px;height:296px;background:var(--footer)}
.foot-brand-name{font-family:"Raleway",sans-serif;font-weight:600;font-size:25px;color:var(--white)}
.foot-desc{left:100px;top:2226px;width:240px;font-size:12px;line-height:22px;color:var(--footer-text)}
.pay{top:2298px;width:40px;height:20px;background:#e9e9e9;border-radius:2px}
.foot-col h4{font-family:"Raleway",sans-serif;font-weight:700;font-size:15px;color:var(--white);margin-bottom:14px}
.foot-col ul{list-style:none}
.foot-col li{font-size:11.5px;line-height:22.5px;color:var(--footer-text)}
.foot-col.links li{text-decoration:underline}
.foot-sep{top:2150px;width:1px;height:165px;background:#3a3a3a}
.contact-row{display:flex;gap:14px;font-size:11.5px;line-height:20px;color:var(--footer-text);margin-bottom:16px}
.foot-rule{left:100px;top:2345px;width:1000px;height:1px;background:#333}
.copy{left:100px;top:2369px;font-size:11.5px;color:var(--footer-text)}
.follow{left:798px;top:2369px;font-size:12px;color:var(--footer-text)}
.social{top:2362px;width:27px;height:27px;background:var(--white);border-radius:4px}
</style>
</head>
<body>
<div class="abs topline"></div>

<header class="abs header">
  <div class="abs brand" style="left:100px;top:36px">
    <span class="brand-mark"></span><span class="brand-name">myQuikTrade</span>
  </div>
  <span class="abs nav-link" style="left:738px;top:24px">How it works</span>
  <span class="abs nav-link" style="left:873px;top:24px">Help</span>
  <span class="abs btn-nav btn-buy" style="left:941px;top:17px;width:74px;height:33px">Buy</span>
  <span class="abs btn-nav btn-sell" style="left:1025px;top:17px;width:75px;height:33px">Sell</span>
  <span class="abs btn-login" style="left:941px;top:69px;width:159px;height:40px">
    <svg width="16" height="16" viewBox="0 0 16 16"><circle cx="8" cy="4.5" r="3.5" fill="#fff"/><path d="M1 16c0-4 3-6.5 7-6.5s7 2.5 7 6.5z" fill="#fff"/></svg>Login/Register
  </span>
</header>

<section class="abs hero">
  <div class="abs hero-photo" role="img" aria-label="Photo of two young friends smiling and looking at their smartphones"></div>
  <svg class="abs hero-red" viewBox="0 0 1200 519" preserveAspectRatio="none">
    <polygon points="0,0 547,0 660,519 0,519" fill="#ec1f27" opacity=".88"/>
  </svg>
  <div class="abs hero-art" role="img" aria-label="White line illustration of a desktop monitor, laptop, tablet and phone"></div>
  <p class="abs hero-text">It is a platform that enables users to sell their old electronics for cash,<br>either for themselves or they can donate the cash to charity.</p>
  <span class="abs btn-hero" style="left:153px">BUY</span>
  <span class="abs hero-or">OR</span>
  <span class="abs btn-hero" style="left:352px">SELL</span>
</section>

<h2 class="abs sec-title" style="top:686px">CLICK YOUR GADGET TO SELL</h2>
<p class="abs sec-text" style="top:733px">Sed ut perspiciatis unde omnis iste natus error sit voluptatem accusantium doloremque laudantium, totam rem aperiam, eaque ipsa quae ab illo inventore veritatis et quasi architecto beatae vitae dicta sunt explicabo.</p>
<svg class="abs" style="left:98px;top:860px" width="20" height="34" viewBox="0 0 20 34"><path d="M17 2L3 17l14 15" fill="none" stroke="#c8c8c8" stroke-width="2"/></svg>
<svg class="abs" style="left:1082px;top:860px" width="20" height="34" viewBox="0 0 20 34"><path d="M3 2l14 15L3 32" fill="none" stroke="#c8c8c8" stroke-width="2"/></svg>
<div class="abs gadget" style="left:177px"><div class="gadget-inner"><svg width="52" height="46" viewBox="0 0 52 46" fill="none" stroke="#fff" stroke-width="3"><rect x="2" y="2" width="48" height="32" rx="2"/><path d="M20 34v8h12v-8M14 43h24"/></svg></div></div>
<div class="abs gadget" style="left:357px"><div class="gadget-inner"><svg width="54" height="38" viewBox="0 0 54 38" fill="none" stroke="#fff" stroke-width="3"><rect x="8" y="2" width="38" height="26" rx="2"/><path d="M2 34h50"/></svg></div></div>
<div class="abs gadget" style="left:537px"><div class="gadget-inner"><svg width="36" height="46" viewBox="0 0 36 46" fill="none" stroke="#fff" stroke-width="3"><rect x="2" y="2" width="32" height="42" rx="4"/><rect x="8" y="8" width="20" height="28"/></svg></div></div>
<div class="abs gadget" style="left:717px"><div class="gadget-inner"><svg width="26" height="48" viewBox="0 0 26 48" fill="none" stroke="#fff" stroke-width="3"><rect x="2" y="2" width="22" height="44" rx="4"/><path d="M6 10h14v26H6z"/><circle cx="13" cy="41" r="1.5" fill="#fff"/></svg></div></div>
<div class="abs gadget" style="left:897px"><div class="gadget-inner"><svg width="66" height="38" viewBox="0 0 66 38"><rect x="2" y="2" width="62" height="34" rx="17" fill="#fff"/><path d="M16 13v12M10 19h12" stroke="#3d3a5c" stroke-width="4"/><circle cx="46" cy="14" r="3" fill="#3d3a5c"/><circle cx="52" cy="21" r="3" fill="#3d3a5c"/><circle cx="40" cy="21" r="3" fill="#3d3a5c"/></svg></div></div>

<section class="abs how"></section>
<h2 class="abs sec-title" style="top:1043px">HOW TO SELL YOUR PRODUCT</h2>
<p class="abs sec-text" style="top:1096px">Sed ut perspiciatis unde omnis iste natus error sit voluptatem accusantium doloremque laudantium, totam rem aperiam, eaque ipsa quae ab illo inventore veritatis et quasi architecto beatae vitae dicta sunt explicabo.</p>
<span class="abs btn-red" style="left:473px;top:1168px;width:254px;height:45px">CLICK HERE TO READ MORE</span>

<section class="abs app" role="img" aria-label="Dim navy-tinted photo of a person using a phone"></section>
<h2 class="abs app-title">MYQUIKTRADE MOBILE APP</h2>
<p class="abs app-text">Lorem ipsum dolor sit amet, consectetur adipiscing elit, sed do eiusmod tempor incididunt ut labore et dolore magna aliqua. Ut enim ad minim veniam, quis nostrud exercitation ullamco laboris nisi ut aliquip ex ea commodo consequat. Duis aute irure dolor in reprehenderit in voluptate velit esse cillum dolore</p>
<span class="abs store-badge" style="left:167px"></span>
<span class="abs store-badge" style="left:330px"></span>
<div class="abs app-device" role="img" aria-label="Hand holding a white smartphone showing the app install screen"></div>

<h2 class="abs sec-title" style="top:1707px">WHY CUSTOMERS CHOOSE US</h2>
<svg class="abs" style="left:200px;top:1780px" width="90" height="66" viewBox="0 0 90 66" fill="#ec1f27">
  <rect x="2" y="26" width="50" height="28"/><path d="M54 32h18l14 12v10H54z"/><circle cx="18" cy="58" r="7"/><circle cx="70" cy="58" r="7"/>
  <circle cx="18" cy="16" r="14"/><path d="M18 8v9h6" stroke="#fff" stroke-width="3" fill="none"/>
</svg>
<svg class="abs" style="left:550px;top:1780px" width="90" height="66" viewBox="0 0 90 66" fill="#ec1f27">
  <rect x="4" y="6" width="64" height="40" rx="5" transform="rotate(-10 36 26)"/>
  <rect x="14" y="16" width="64" height="40" rx="5"/><rect x="14" y="24" width="64" height="7" fill="#fff"/>
  <rect x="58" y="40" width="24" height="20" rx="2"/><path d="M62 40v-6a8 8 0 0 1 16 0v6" stroke="#ec1f27" stroke-width="3" fill="none"/>
</svg>
<svg class="abs" style="left:920px;top:1788px" width="76" height="52" viewBox="0 0 76 52">
  <rect x="2" y="2" width="72" height="48" fill="#ec1f27"/><rect x="10" y="9" width="56" height="34" fill="none" stroke="#fff" stroke-width="2"/>
  <circle cx="38" cy="26" r="12" fill="#fff"/><path d="M36 20h3v13" stroke="#ec1f27" stroke-width="3" fill="none"/>
</svg>
<div class="abs feature" style="left:71px;top:1866px"><h3>FAST DELIVERY</h3><p>Our standard delivery service is FREE in UK, regardless of the size and value. We are committed to offering fast and free delivery.</p></div>
<div class="abs feature" style="left:430px;top:1866px"><h3>SAFE &amp; SECURE PAYMENT</h3><p>Here at myQuikTrade we like to ensure that our customers can purchase from us with confidence &amp; 100% safe and secure payment methods.</p></div>
<div class="abs feature" style="left:787px;top:1866px"><h3>100% MONEY BACK GUARANTED</h3><p>To prove our confidence in the services we provide, we are offering a generous 60 day, money back, satisfaction guarantee!</p></div>

<section class="abs news"></section>
<svg class="abs" style="left:97px;top:2053px" width="46" height="38" viewBox="0 0 46 38"><g transform="rotate(-12 23 19)"><rect x="3" y="6" width="40" height="27" rx="2" fill="#fff"/><path d="M3 8l20 14 20-14" stroke="#ec1f27" stroke-width="2.5" fill="none"/></g></svg>
<span class="abs news-small">NEWSLETTER</span>
<span class="abs news-big">SUBSCRIPTION</span>
<span class="abs news-input">ENTER EMAIL ADDRESS</span>
<span class="abs news-btn">SUBSCRIBE</span>

<footer class="abs footer"></footer>
<div class="abs brand" style="left:100px;top:2175px">
  <span class="brand-mark"></span><span class="foot-brand-name">myQuikTrade</span>
</div>
<p class="abs foot-desc">At vero eos et accusamus et iusto odio dignissimos ducimus qui blan</p>
<span class="abs pay" style="left:100px"></span>
<span class="abs pay" style="left:145px"></span>
<span class="abs pay" style="left:190px"></span>
<span class="abs pay" style="left:235px;width:50px"></span>

<span class="abs foot-sep" style="left:346px"></span>
<span class="abs foot-sep" style="left:531px"></span>
<span class="abs foot-sep" style="left:692px"></span>
<span class="abs foot-sep" style="left:909px"></span>

<div class="abs foot-col links" style="left:375px;top:2152px"><h4>QUICK LINKS</h4><ul><li>Contact</li><li>FAQ</li><li>Delivery</li><li>Returns</li><li>Track Orders</li><li>Subscribe</li></ul></div>
<div class="abs foot-col" style="left:561px;top:2152px"><h4>EXTRAS</h4><ul><li>Specials</li><li>New products</li><li>Top sellers</li><li>Our stores</li><li>Contact us</li><li>About us</li></ul></div>
<div class="abs foot-col" style="left:724px;top:2152px"><h4>MY ACCOUNT</h4><ul><li>Delivery Information</li><li>Privacy Policy</li><li>Returns Policy</li><li>Terms and Conditions</li><li>FAQs</li></ul></div>
<div class="abs foot-col" style="left:939px;top:2152px"><h4>CONTACT US</h4>
  <div class="contact-row"><svg width="10" height="14" viewBox="0 0 10 14" style="margin-top:4px"><path d="M5 0a5 5 0 0 1 5 5c0 4-5 9-5 9S0 9 0 5a5 5 0 0 1 5-5z" fill="#fff"/><circle cx="5" cy="5" r="2" fill="#1f1f1f"/></svg><span>418 Wrenfield Ave.<br>Marlowe Bay, CA 94870</span></div>
  <div class="contact-row"><svg width="11" height="12" viewBox="0 0 11 12" style="margin-top:4px"><path d="M2 0l2 3-1 2c1 2 2 3 4 4l2-1 2 2-2 2C4 12-1 6 0 2z" fill="#fff"/></svg><span>1 555 204 7781</span></div>
  <div class="contact-row"><svg width="12" height="10" viewBox="0 0 12 10" style="margin-top:5px"><rect width="12" height="10" fill="#fff"/><path d="M0 1l6 4 6-4" stroke="#1f1f1f" fill="none"/></svg><span style="text-decoration:underline">hello@quiktrademail.com</span></div>
</div>

<span class="abs foot-rule"></span>
<span class="abs copy">Copyrights © 2016, myQuikTrade.&nbsp; All Rights Reserved</span>
<span class="abs follow">Follow us on :</span>
<span class="abs social" style="left:894px"></span>
<span class="abs social" style="left:929px"></span>
<span class="abs social" style="left:964px"></span>
<span class="abs social" style="left:999px"></span>
<span class="abs social" style="left:1034px"></span>
<span class="abs social" style="left:1069px"></span>
</body>
</html>
```